Travesco Business Cards

We need a business card design for Travesco Mining.

This is a B2B company that buys and sells large machinery tires within the coal mining industry. The design should the strong, crisp and masculine. I have uploaded the company logo and rough mock-up of what the back of the card should look like. the front of the card should have the same look/feel as the back. I need editable templates for both the front and the back of the card.

Color scheme should be grey/green/black

Contact information to include on the card:
Name: Dale Pemberton
Title: Managing Director
Phone: 214-503-6192
Address: 1185 Wexley #3 Dallas, TX 75211
Email: Dale@Travesco-example.com

I am also opening a contest for letterhead design. If you submit a business card design, please also submit a letterhead design with the same look/feel. The winner of the business card design will also will the letter head and be paid for both.

Target Market(s)

Procurement men/women in the coal mining industry

Industry/Entity Type

Coal Mining

```html
<!DOCTYPE html>
<html lang="en">
<head>
<meta charset="utf-8">
<title>Travesco Mining – Stationery Set</title>
<link rel="stylesheet" href="https://fonts.googleapis.com/css2?family=Teko:wght@400;500;600&family=Carlito:wght@400;700&display=swap">
<style>
  :root {
    --backdrop: #2b2b2b;
    --paper: #ffffff;
    --slate: #7d7f7e;
    --slate-dark: #4f5150;
    --card-grey-top: #6c6d6d;
    --card-grey-bottom: #4b4c4c;
    --green: #6ab43e;
    --green-light: #8fce5c;
    --ink: #1d1d1d;
    --black: #0b0b0b;
    --soft-white: #e9e9e9;
    --display: "Teko", "Arial Narrow", sans-serif;
    --body: "Carlito", "Calibri", sans-serif;
  }
  * { margin: 0; padding: 0; box-sizing: border-box; }
  html, body { width: 1200px; height: 1000px; overflow: hidden; }
  body { background: var(--backdrop); position: relative; font-family: var(--body); }

  .brand { display: flex; align-items: center; position: absolute; }
  .brand-mark { background: var(--green); flex: none; }
  .brand-name { font-family: var(--display); font-weight: 600; line-height: 1; letter-spacing: 0.04em; white-space: nowrap; }

  /* hero brand */
  .hero-brand { left: 636px; top: 30px; gap: 18px; width: 530px; }
  .hero-brand .brand-mark { width: 76px; height: 76px; }
  .hero-brand .brand-name { color: #fff; font-size: 58px; padding-top: 9px; }

  /* letterhead */
  .letterhead { position: absolute; left: 60px; top: 57px; width: 508px; height: 659px; background: var(--paper); }
  .lh-header { position: absolute; left: 0; top: 0; width: 100%; height: 81px; background: var(--slate); border-bottom: 3px solid var(--green); }
  .lh-header .brand { left: 132px; top: 16px; gap: 9px; }
  .lh-header .brand-mark { width: 26px; height: 26px; }
  .lh-header .brand-name { color: #fff; font-size: 26px; padding-top: 4px; }
  .lh-contact { position: absolute; left: 0; top: 62px; width: 100%; text-align: center; font-size: 5.5px; color: #f2f2f2; letter-spacing: 0.05em; text-transform: uppercase; }
  .lh-date { position: absolute; right: 57px; top: 123px; font-size: 9px; color: var(--ink); }
  .lh-body { position: absolute; left: 40px; top: 168px; width: 410px; font-size: 8.4px; line-height: 1.42; color: var(--ink); }
  .lh-body p { margin-bottom: 11px; }
  .lh-body p.tight { margin-bottom: 0; }
  .lh-footer { position: absolute; left: 0; bottom: 0; width: 100%; height: 50px; background: var(--slate); border-top: 3px solid var(--green); }
  .lh-footer .brand { left: 36px; top: 12px; gap: 7px; }
  .lh-footer .brand-mark { width: 20px; height: 20px; }
  .lh-footer .brand-name { color: #fff; font-size: 21px; padding-top: 3px; }
  .lh-footer-contact { position: absolute; left: 380px; top: 12px; font-size: 5.5px; line-height: 1.55; color: #f2f2f2; text-transform: uppercase; letter-spacing: 0.05em; }

  /* envelope */
  .envelope { position: absolute; left: 52px; top: 740px; width: 526px; height: 228px; background: var(--paper); overflow: hidden; }
  .envelope .brand { left: 14px; top: 12px; gap: 6px; }
  .envelope .brand-mark { width: 20px; height: 20px; }
  .envelope .brand-name { color: var(--ink); font-size: 20px; padding-top: 3px; }
  .env-address { position: absolute; left: 46px; top: 38px; font-size: 7px; color: var(--ink); }
  .env-swoosh { position: absolute; left: 0; bottom: 0; width: 526px; height: 90px; }

  /* business card front */
  .card-front { position: absolute; left: 645px; top: 224px; width: 471px; height: 268px; background: linear-gradient(160deg, var(--card-grey-top), var(--card-grey-bottom)); overflow: hidden; }
  .card-front .brand { left: 56px; top: 24px; gap: 12px; }
  .card-front .brand-mark { width: 48px; height: 48px; }
  .card-front .brand-name { color: var(--soft-white); font-size: 42px; padding-top: 7px; }
  .card-person { position: absolute; left: 33px; top: 96px; font-family: var(--display); line-height: 1; }
  .card-name { font-size: 27px; font-weight: 500; color: var(--soft-white); letter-spacing: 0.05em; text-transform: uppercase; }
  .card-title { font-size: 17px; color: var(--green-light); letter-spacing: 0.05em; text-transform: uppercase; margin-top: 2px; }
  .card-contacts { position: absolute; left: 32px; top: 162px; list-style: none; font-family: var(--display); font-size: 14px; color: var(--soft-white); letter-spacing: 0.04em; }
  .card-contacts li { display: flex; align-items: flex-start; gap: 6px; margin-bottom: 6px; line-height: 1.05; }
  .card-contacts svg { flex: none; width: 14px; height: 14px; }
  .card-rule { position: absolute; left: 0; bottom: 0; width: 100%; height: 17px; background: var(--green); border-top: 3px solid #f4f4f4; }

  /* business card back */
  .card-back { position: absolute; left: 645px; top: 551px; width: 471px; height: 268px; background: var(--black); overflow: hidden; }
  .card-back .texture { position: absolute; inset: 0; background: radial-gradient(circle at 50% 50%, #1c1c1c, var(--black)); }
  .card-back .brand { left: 33px; top: 105px; gap: 16px; }
  .card-back .brand-mark { width: 60px; height: 60px; }
  .card-back .brand-name { color: #fff; font-size: 48px; padding-top: 8px; }
</style>
</head>
<body>

  <div class="brand hero-brand">
    <span class="brand-mark"></span>
    <span class="brand-name">TRAVESCO MINING</span>
  </div>

  <section class="letterhead">
    <header class="lh-header">
      <div class="brand">
        <span class="brand-mark"></span>
        <span class="brand-name">TRAVESCO MINING</span>
      </div>
      <p class="lh-contact">214-503-6192 &nbsp;|&nbsp; 1185 Wexley #3 Dallas, TX 75211 &nbsp;|&nbsp; Dale@Travesco-example.com</p>
    </header>

    <p class="lh-date">Wednesday, October 09, 2013</p>

    <div class="lh-body">
      <p>We need a business card design for Travesco Mining.</p>
      <p>This is a B2B company that buys and sells large machinery tires within the coal mining industry. The design should the strong, crisp and masculine. I have uploaded the company logo and rough mock-up of what the back of the card should look like. the front of the card should have the same look/feel as the back. I need editable templates for both the front and the back of the card.</p>
      <p>Color scheme should be grey/green/black</p>
      <p style="margin-top:22px" class="tight">I am also opening a contest for letterhead design. If you submit a business card design, please also submit a letterhead design with the same look/feel. The winner of the business card design will also will the letter head and be paid for both.</p>
      <p class="tight">Deadline</p>
      <p class="tight">Wednesday, October 09, 2013</p>
      <p class="tight">Target Market(s)</p>
      <p class="tight">Procurement men/women in the coal mining industry</p>
      <p class="tight">Look and Feel</p>
      <p>Each slider illustrates characteristics of the customer's brand and the style your design should communicate.</p>
      <p style="margin-top:26px" class="tight">Contact information to include on the card:</p>
      <p class="tight">Name: Dale Pemberton</p>
      <p class="tight">Title: Managing Director</p>
      <p class="tight">Phone: 214-503-6192</p>
      <p class="tight">Address: 1185 Wexley #3 Dallas, TX 75211</p>
      <p class="tight">Email: Dale@Travesco-example.com</p>
    </div>

    <footer class="lh-footer">
      <div class="brand">
        <span class="brand-mark"></span>
        <span class="brand-name">TRAVESCO MINING</span>
      </div>
      <p class="lh-footer-contact">214-503-6192<br>Dale@Travesco-example.com<br>1185 Wexley #3 Dallas, TX 75211</p>
    </footer>
  </section>

  <section class="envelope">
    <div class="brand">
      <span class="brand-mark"></span>
      <span class="brand-name">TRAVESCO MINING</span>
    </div>
    <p class="env-address">1185 Wexley #3 Dallas, TX 75211</p>
    <svg class="env-swoosh" viewBox="0 0 526 90" preserveAspectRatio="none" aria-hidden="true">
      <path d="M0 36 Q260 4 526 22 L526 90 L0 90 Z" fill="#8a8a8a"/>
      <path d="M0 44 Q250 12 526 30 L526 90 L0 90 Z" fill="#111"/>
      <path d="M0 68 Q230 40 526 56 L526 90 L0 90 Z" fill="#fff"/>
      <path d="M0 76 Q220 56 420 90 L0 90 Z" fill="#6ab43e"/>
    </svg>
  </section>

  <section class="card-front">
    <div class="brand">
      <span class="brand-mark"></span>
      <span class="brand-name">TRAVESCO MINING</span>
    </div>
    <div class="card-person">
      <p class="card-name">Dale Pemberton</p>
      <p class="card-title">Managing Director</p>
    </div>
    <ul class="card-contacts">
      <li>
        <svg viewBox="0 0 14 14" aria-hidden="true"><circle cx="7" cy="7" r="7" fill="#6ab43e"/><path d="M4.3 3.6l1.4-.2.7 1.7-.9.7c.4.9 1.1 1.6 2 2l.7-.9 1.7.7-.2 1.4c-3 .2-5.6-2.4-5.4-5.4z" fill="#fff"/></svg>
        <span>: 214.503.6192</span>
      </li>
      <li>
        <svg viewBox="0 0 14 14" aria-hidden="true"><circle cx="7" cy="7" r="7" fill="#6ab43e"/><rect x="3.5" y="4.5" width="7" height="5" fill="#fff"/><path d="M3.5 4.5l3.5 2.8 3.5-2.8" fill="none" stroke="#6ab43e" stroke-width=".8"/></svg>
        <span>: Dale@Travesco-example.com</span>
      </li>
      <li>
        <svg viewBox="0 0 14 14" aria-hidden="true"><circle cx="7" cy="7" r="7" fill="#6ab43e"/><path d="M7 3a2.4 2.4 0 0 1 2.4 2.4C9.4 7.3 7 10.6 7 10.6S4.6 7.3 4.6 5.4A2.4 2.4 0 0 1 7 3z" fill="#fff"/><circle cx="7" cy="5.4" r=".9" fill="#6ab43e"/></svg>
        <span>: 1185 Wexley #3<br>Dallas, TX 75211</span>
      </li>
    </ul>
    <div class="card-rule"></div>
  </section>

  <section class="card-back">
    <div class="texture" role="img" aria-label="Fine dark dot texture across the card back"></div>
    <div class="brand">
      <span class="brand-mark"></span>
      <span class="brand-name">TRAVESCO MINING</span>
    </div>
  </section>

</body>
</html>
```